Tarnwick is a steel frame construction company that builds residential and commercial homes

1. Homepage (we are after a basic website)
Hero Section:
A full-width image or video showcasing steel frames in construction or a finished project.
Tagline: Short, impactful tagline (e.g., "Strong Structures for Tomorrow").
Call-to-Action (CTA): A prominent "Get a Quote" or "Contact Us" button.
About Us (Snapshot Section):

A few lines about the company, emphasizing experience, certifications, and commitment to quality.
Include a "Learn More" button linking to the detailed About Us page.
Products/Services Section:

Feature the main products like steel frames for industrial, residential, and commercial projects.
Each category should have a "Learn More" link to a dedicated product page.
Project Showcase/Portfolio:

Display 2-3 featured projects with images, descriptions, and a "View All Projects" button.
Certifications & Partners:

Display logos of certifications (QSB, local building standards) and partnerships with construction companies or industry bodies.
Footer:

Contact information, quick links (Home, About, Products, Services, Contact), and social media icons.
2. Products Page
Overview:

A grid or list layout showing different steel frame products or services.
Each product should have a title, brief description, and a thumbnail image.
Individual Product Pages:

Detailed information on specific products (e.g., “Steel Frames for Residential Construction”):
Features: Highlight specific features like durability, eco-friendliness, precision, etc.
Technical Specs: Material grades, dimensions, finishes available.
Case Studies: A couple of client testimonials or case studies of where this product was used.
Downloadable Resources:

Technical datasheets or catalogs for users to download.
Include a form to capture user information before they download the document (optional for lead generation).
3. Projects/Portfolio Page
Gallery of Projects:
Display completed projects with high-quality images, each linked to a project detail page.
Filter options (e.g., industrial, residential, commercial).
Project Detail Pages:
A detailed description of the project, challenges, and how the steel frames were used.
other website we liked are:
https://www.tarnwickbuilds.example/
https://orlenbayhomes.example/

1. Objective:
Create an informative, professional, and visually appealing website that promotes steel frame construction solutions, showcasing the company’s offerings, expertise, and projects.
The website should highlight the benefits of steel frames (e.g., durability, sustainability, and cost-efficiency) and cater to both B2B and B2C clients.
2. Target Audience:
Primary: Architects, builders, and construction companies.
Secondary: Homeowners, investors, and property developers looking for modern, durable construction solutions.

```html
<!DOCTYPE html>
<html lang="en">
<head>
<meta charset="utf-8">
<title>Tarnwick | Steel Frame Construction</title>
<link href="https://fonts.googleapis.com/css2?family=Montserrat:wght@400;600;700;800&family=Roboto:wght@400;500;700&display=swap" rel="stylesheet">
<style>
:root{
  --blue:#1f6fc0;
  --blue-dark:#1559a3;
  --ink:#222a33;
  --text:#4a4f55;
  --muted:#8a8f95;
  --light:#f3f3f3;
  --grey-band:#d6d6d6;
  --white:#ffffff;
}
*{box-sizing:border-box;margin:0;padding:0}
html,body{width:1200px;height:3312px;overflow:hidden;background:var(--white)}
body{font-family:"Roboto",sans-serif;color:var(--text);position:relative}
.canvas{position:relative;width:1200px;height:3312px;overflow:hidden}
.abs{position:absolute}

/* top bar */
.topbar{top:0;left:0;width:1200px;height:40px;background:var(--blue);color:var(--white);font-size:15px;display:flex;justify-content:flex-end;align-items:center;gap:22px;padding-right:112px}
.topbar .item{display:flex;align-items:center;gap:8px}
.topbar .sep{opacity:.7}

/* header */
.header{top:40px;left:0;width:1200px;height:100px;background:var(--white);display:flex;align-items:center;padding:0 112px}
.brand{display:flex;align-items:center;gap:10px;font-family:"Montserrat",sans-serif;font-weight:800;font-size:30px;color:var(--blue);letter-spacing:1px}
.brand .mark{width:22px;height:22px;background:var(--blue)}
.nav{margin-left:auto;display:flex;align-items:center;gap:34px;font-family:"Montserrat",sans-serif;font-weight:600;font-size:15px;color:var(--ink)}
.nav .active{background:var(--light);padding:14px 18px;color:var(--blue)}
.btn-quote{margin-left:30px;border:2px solid var(--blue);color:var(--blue);padding:14px 20px;font-family:"Montserrat",sans-serif;font-weight:700;font-size:15px}

/* hero */
.hero-photo{top:140px;left:0;width:1200px;height:620px;background:linear-gradient(160deg,#3f4a3a 0%,#6d7660 35%,#9a9a8c 60%,#5b6450 100%)}
.hero-shape{top:560px;left:0;width:1200px;height:220px}
.hero-frame{top:280px;left:272px;width:656px;height:178px;border:2px solid rgba(255,255,255,.45)}
.hero-title{top:300px;left:0;width:1200px;text-align:center;color:var(--white);font-family:"Montserrat",sans-serif;line-height:1.1}
.hero-title .l1{font-weight:800;font-size:56px;letter-spacing:2px}
.hero-title .l2{font-weight:400;font-size:56px;letter-spacing:3px}
.btn-contact{top:448px;left:530px;width:140px;height:52px;background:var(--blue);color:var(--white);font-family:"Montserrat",sans-serif;font-weight:700;font-size:15px;display:flex;align-items:center;justify-content:center}
.play{top:544px;left:572px;width:56px;height:56px}

/* section titles */
.sec-title{display:flex;align-items:center;font-family:"Montserrat",sans-serif;font-weight:800;font-size:52px;line-height:1}
.sec-title .box{background:var(--blue);color:var(--white);padding:6px 10px 4px}
.sec-title .rest{color:var(--blue);padding-left:6px}
.sec-title.light .rest{color:var(--white);-webkit-text-stroke:0}
.title-line{height:3px;background:var(--blue)}

/* about */
.about{top:800px;left:0;width:1200px;height:580px;background:var(--light)}
.about-frame{top:820px;left:150px;width:420px;height:470px;border:2px solid #c9c9c9}
.about-img1{top:832px;left:112px;width:464px;height:440px;background:linear-gradient(180deg,#cfe0ef 0%,#b8c8d4 55%,#8f9a85 100%);border:6px solid var(--white)}
.about-img2{top:1072px;left:356px;width:284px;height:256px;background:linear-gradient(180deg,#c7d9ea 0%,#c4ad8a 60%,#8b7a61 100%);border:6px solid var(--white)}
.about-title{top:868px;left:724px}
.about-text{top:970px;left:724px;width:370px;font-size:16px;line-height:1.65;color:var(--text)}
.about-text p{margin-bottom:18px}
.btn-outline{border:2px solid var(--blue);color:var(--blue);font-family:"Montserrat",sans-serif;font-weight:700;font-size:15px;display:flex;align-items:center;justify-content:center;background:var(--white)}
.about-btn{top:1248px;left:724px;width:148px;height:56px}

/* products */
.products-title{top:1500px;left:0;width:1200px;display:flex;justify-content:center}
.card-img{width:476px;height:360px}
.card-name{font-family:"Montserrat",sans-serif;font-weight:700;font-size:22px;color:var(--ink)}
.card-btn{width:148px;height:52px}
.card-btn.filled{background:#9b9b9b;border-color:#9b9b9b;color:var(--white)}

/* projects */
.projects{top:2200px;left:0;width:1200px;height:708px;background:linear-gradient(135deg,#cfcfcf 0%,#e4e4e4 50%,#cbcbcb 100%)}
.projects-title{top:2268px;left:0;width:1200px;display:flex;justify-content:center}
.proj-name{font-family:"Montserrat",sans-serif;font-weight:700;font-size:22px;color:var(--ink);text-align:center;width:476px}

/* benefits */
.benefits{top:2908px;left:0;width:1200px;height:152px;background:var(--blue);display:flex;align-items:center;padding:0 112px;gap:0}
.benefit{display:flex;align-items:center;gap:26px;width:356px;color:var(--white);font-family:"Montserrat",sans-serif;font-weight:700;font-size:22px}
.benefit .icon{width:80px;height:80px;background:var(--white);display:flex;align-items:center;justify-content:center}

/* footer */
.footer-brand{top:3136px;left:112px}
.footer-nav{top:3128px;left:452px;width:636px;display:flex;justify-content:flex-end;gap:26px;font-family:"Montserrat",sans-serif;font-weight:600;font-size:17px;color:var(--ink)}
.footer-nav .sep{color:var(--muted)}
.footer-contact{top:3176px;left:452px;width:636px;display:flex;justify-content:flex-end;gap:22px;font-size:15px;color:var(--ink)}
.footer-contact .item{display:flex;align-items:center;gap:8px}
.copyright{top:3260px;left:0;width:1200px;height:52px;background:var(--light);display:flex;align-items:center;justify-content:center;font-size:14px;color:var(--ink)}
</style>
</head>
<body>
<div class="canvas">

  <div class="abs topbar">
    <span class="item"><svg width="16" height="16" viewBox="0 0 24 24" fill="#fff"><path d="M6.6 10.8a15.1 15.1 0 006.6 6.6l2.2-2.2a1 1 0 011-.25 11.4 11.4 0 003.6.57 1 1 0 011 1V20a1 1 0 01-1 1A17 17 0 013 4a1 1 0 011-1h3.5a1 1 0 011 1c0 1.25.2 2.45.57 3.57a1 1 0 01-.25 1z"/></svg>Call Us: +1 (000) 000 0000</span>
    <span class="sep">|</span>
    <span class="item"><svg width="16" height="16" viewBox="0 0 24 24" fill="#fff"><path d="M3 5h18v14H3z" opacity=".0"/><path d="M3 5h18a1 1 0 011 1v12a1 1 0 01-1 1H3a1 1 0 01-1-1V6a1 1 0 011-1zm9 7l8-5H4z"/></svg>Email Us: info@tarnwick.example</span>
  </div>

  <header class="abs header">
    <div class="brand"><span class="mark"></span>TARNWICK</div>
    <nav class="nav">
      <span class="active">HOME</span><span>ABOUT</span><span>PRODUCTS</span><span>SERVICES</span><span>CONTACT</span>
    </nav>
    <span class="btn-quote">GET A QUOTE</span>
  </header>

  <div class="abs hero-photo" role="img" aria-label="Aerial view of a steel frame house under construction among trees"></div>
  <svg class="abs hero-shape" viewBox="0 0 1200 220" preserveAspectRatio="none">
    <polygon points="0,20 600,180 1200,20 1200,220 0,220" fill="#ffffff"/>
    <polygon points="440,150 600,192 760,150 760,160 600,204 440,160" fill="#1f6fc0"/>
  </svg>
  <div class="abs hero-frame"></div>
  <div class="abs hero-title"><div class="l1">STRONG STRUCTURES</div><div class="l2">FOR TOMORROW</div></div>
  <div class="abs btn-contact">CONTACT US</div>
  <svg class="abs play" viewBox="0 0 56 56"><circle cx="28" cy="28" r="28" fill="#fff"/><polygon points="22,17 40,28 22,39" fill="#222a33"/></svg>

  <section class="abs about"></section>
  <div class="abs about-frame"></div>
  <div class="abs about-img1" role="img" aria-label="Large steel portal frame structure against blue sky"></div>
  <div class="abs about-img2" role="img" aria-label="Steel roof trusses on a brick home"></div>
  <div class="abs about-title">
    <div class="sec-title"><span class="box">ABOUT</span><span class="rest">US</span></div>
  </div>
  <div class="abs about-text">
    <p>Lorem ipsum dolor sit amet, consectetur adipiscing elit, sed do eiusmod tempor incididunt ut labore et dolore magna aliqua. Ut enim ad minim veniam, quis nostrud exercitation ullamco laboris nisi ut aliquip ex ea commodo consequat. Duis aute irure dolor in reprehenderit in voluptate velit esse dolor nulla pariatur.</p>
    <p>Lorem ipsum dolor sit amet, consectetur adipiscing elit, sed do eiusmod tempor incididunt ut labore et dolore magna aliqua nulla pariatur.</p>
  </div>
  <div class="abs btn-outline about-btn">LEARN MORE</div>

  <div class="abs products-title">
    <div class="sec-title"><span class="box">OUR</span><span class="rest">PRODUCTS</span></div>
  </div>
  <div class="abs card-img" style="top:1640px;left:112px;background:linear-gradient(180deg,#a9c8e6 0%,#c7d6e2 45%,#b5865c 80%,#9c6f48 100%)" role="img" aria-label="Light gauge steel wall frames on a building site"></div>
  <div class="abs card-img" style="top:1640px;left:612px;background:linear-gradient(180deg,#dfe6ec 0%,#c9ced2 45%,#2b2f33 75%,#8a8d8f 100%)" role="img" aria-label="Modern prefab cabin home with glass front"></div>
  <div class="abs card-name" style="top:2016px;left:188px">CUSTOM FRAMES</div>
  <div class="abs card-name" style="top:2016px;left:688px">PREFAB HOMES</div>
  <div class="abs btn-outline card-btn" style="top:2068px;left:188px">LEARN MORE</div>
  <div class="abs btn-outline card-btn filled" style="top:2068px;left:688px">LEARN MORE</div>

  <section class="abs projects"></section>
  <div class="abs projects-title">
    <div class="sec-title"><span class="box">OUR</span><span class="rest" style="color:#ffffff">PROJECTS</span></div>
  </div>
  <div class="abs card-img" style="top:2400px;left:112px;background:linear-gradient(180deg,#b9d3ea 0%,#d8d8d4 50%,#9aa08c 100%)" role="img" aria-label="Two-storey block house with dark roof under construction"></div>
  <div class="abs card-img" style="top:2400px;left:612px;background:linear-gradient(180deg,#c5daf0 0%,#b7c9d8 45%,#a9a9a4 100%)" role="img" aria-label="House with steel roof framing being installed"></div>
  <div class="abs proj-name" style="top:2784px;left:112px">12 HARLOW LANE BRENFIELD VIC 3810</div>
  <div class="abs proj-name" style="top:2784px;left:612px">465, LORUM IPSUM, UNITED STATES</div>

  <section class="abs benefits">
    <div class="benefit"><span class="icon"><svg width="44" height="44" viewBox="0 0 24 24" fill="none" stroke="#1f6fc0" stroke-width="2"><rect x="3" y="10" width="5" height="4" rx="1"/><rect x="16" y="10" width="5" height="4" rx="1"/><path d="M8 12h8M5 8v8M19 8v8"/></svg></span>DURABILITY</div>
    <div class="benefit"><span class="icon"><svg width="44" height="44" viewBox="0 0 24 24" fill="none" stroke="#1f6fc0" stroke-width="2"><circle cx="12" cy="12" r="4"/><path d="M12 2v4M12 18v4M2 12h4M18 12h4M5 5l3 3M16 16l3 3M19 5l-3 3M8 16l-3 3"/></svg></span>SUSTAINABILITY</div>
    <div class="benefit"><span class="icon"><svg width="44" height="44" viewBox="0 0 24 24" fill="none" stroke="#1f6fc0" stroke-width="2"><circle cx="12" cy="12" r="9"/><path d="M15 9h-4a2 2 0 000 4h2a2 2 0 010 4H9M12 6v2M12 17v2"/></svg></span>COST-EFFICIENCY</div>
  </section>

  <div class="abs footer-brand"><div class="brand"><span class="mark"></span>TARNWICK</div></div>
  <nav class="abs footer-nav"><span>HOME</span><span class="sep">|</span><span>ABOUT</span><span class="sep">|</span><span>PRODUCTS</span><span class="sep">|</span><span>SERVICES</span><span class="sep">|</span><span>CONTACT</span></nav>
  <div class="abs footer-contact">
    <span class="item"><svg width="15" height="15" viewBox="0 0 24 24" fill="#1f6fc0"><path d="M6.6 10.8a15.1 15.1 0 006.6 6.6l2.2-2.2a1 1 0 011-.25 11.4 11.4 0 003.6.57 1 1 0 011 1V20a1 1 0 01-1 1A17 17 0 013 4a1 1 0 011-1h3.5a1 1 0 011 1c0 1.25.2 2.45.57 3.57a1 1 0 01-.25 1z"/></svg>Call Us: +1 (000) 000 0000</span>
    <span>|</span>
    <span class="item"><svg width="15" height="15" viewBox="0 0 24 24" fill="#1f6fc0"><path d="M3 5h18a1 1 0 011 1v12a1 1 0 01-1 1H3a1 1 0 01-1-1V6a1 1 0 011-1zm9 7l8-5H4z"/></svg>Email Us: info@tarnwick.example</span>
  </div>
  <div class="abs copyright">Copyright © 2024 TARNWICK | All Rights Reserved</div>

</div>
</body>
</html>
```